13 Tavo - new website design project

Our company Tavo Electrical is developing a new lead generation website focused on Electrical, LED Lighting and Solar Power. We need a high converting website.

Example of our current website is www.tavoelectrical.com.au You can take content from this website for this new design. Our colours are red, black and white. For our new website we would like to promote Tavo, Bright Days Ahead. Please listen to the jingle.

The below link is the company jingle that we have developed.
http://www.tunecraftaudio.com.au/tav-tc-v1/

The key for this brief is to generate leads for Electrical, LED Lighting (for commercial) and Solar Power & Storage.

Target Market(s)

Business owners in Melbourne Victoria

Number of Pages Required

4 page

Colors
ec1f27
ffffff

Requirements
Must have
• This page must be clean, be in line with company branding and a high converting lead website.

```html
<!DOCTYPE html>
<html lang="en">
<head>
<meta charset="utf-8">
<title>Tavo Electrical</title>
<link rel="stylesheet" href="https://fonts.googleapis.com/css2?family=Roboto:ital,wght@0,300;0,400;0,500;0,700;1,300&display=swap">
<style>
:root{
  --red:#ec1f27;
  --red-soft:#e9474c;
  --red-light:#f07b7b;
  --ink:#1d1d1f;
  --text:#3b3b3b;
  --muted:#6b6b6b;
  --white:#ffffff;
  --grey-bg:#f4f5f7;
  --line:#e0e0e0;
}
*{margin:0;padding:0;box-sizing:border-box}
html,body{width:1200px;height:2347px;overflow:hidden}
body{font-family:"Roboto",Arial,sans-serif;color:var(--text);background:var(--white);position:relative}
section,header,footer{position:absolute;left:0;width:1200px}

/* hero */
.hero{top:0;height:541px;overflow:hidden}
.hero-photo{position:absolute;inset:0;background:linear-gradient(100deg,#6f8fb4 0%,#9db3c9 22%,#4b6a90 40%,#22305a 58%,#14204a 75%,#2b2a2a 100%)}
.hero-ground{position:absolute;left:0;right:0;bottom:0;height:230px;background:linear-gradient(180deg,rgba(40,60,90,0) 0%,rgba(25,35,55,.55) 60%,rgba(30,28,25,.8) 100%)}
.hero-circle{position:absolute;left:455px;top:150px;width:290px;height:290px;border-radius:50%;background:rgba(255,255,255,.12)}
.topbar{position:absolute;left:0;top:0;width:1200px;height:64px;border-bottom:1px solid rgba(255,255,255,.35)}
.brand{position:absolute;left:55px;top:14px;display:flex;align-items:center;gap:8px;color:var(--white);font-weight:700;font-size:30px;letter-spacing:1px}
.brand-dot{width:22px;height:22px;border-radius:50%;background:var(--red)}
.nav{position:absolute;left:352px;top:22px;display:flex;gap:34px}
.nav a{color:var(--white);text-decoration:none;font-size:15px;font-weight:500}
.call{position:absolute;left:1048px;top:14px;width:105px;height:33px;border-radius:17px;background:var(--white);color:var(--ink);font-size:13px;display:flex;align-items:center;justify-content:center}
.hero-title{position:absolute;left:400px;top:165px;width:400px;text-align:center;color:var(--white);line-height:1.1}
.hero-title span{display:block;font-weight:300;font-size:35px;letter-spacing:2px}
.hero-title strong{display:block;font-weight:700;font-size:46px;letter-spacing:2px}

/* section heads */
.sec-title{position:absolute;left:0;width:1200px;text-align:center;font-size:22px;font-weight:500;color:var(--ink)}
.sec-title em{font-style:normal;color:var(--red)}
.dots{position:absolute;left:52px;width:1096px;border-top:1.5px dashed var(--red-soft)}

/* welcome */
.welcome{top:541px;height:110px}
.welcome p{position:absolute;left:52px;top:64px;width:1096px;text-align:center;font-size:13px;line-height:20px;font-weight:300;color:var(--text)}

/* services */
.services{top:651px;height:335px;background:var(--grey-bg)}
.service{position:absolute;top:116px;width:347px;height:175px}
.service-photo{position:absolute;left:0;top:0;width:347px;height:153px;border-radius:4px}
.service-icon{position:absolute;left:150px;top:-23px;width:46px;height:46px;border-radius:50%;background:var(--red);display:flex;align-items:center;justify-content:center}
.service-btn{position:absolute;left:14px;top:133px;width:319px;height:42px;border-radius:4px;background:linear-gradient(90deg,var(--red-soft),var(--red-light));color:var(--white);font-size:17px;font-weight:500;display:flex;align-items:center;justify-content:center}

/* why */
.why{top:986px;height:375px}
.why-link{position:absolute;top:130px;height:1px;background:var(--red-soft)}
.why-item{position:absolute;top:84px;width:260px;text-align:center}
.why-badge{margin:0 auto;width:94px;height:94px;border-radius:50%;background:linear-gradient(135deg,var(--red),var(--red-light));display:flex;align-items:center;justify-content:center;box-shadow:0 0 0 5px #fde3e3}
.why-item h3{margin-top:16px;font-size:18px;font-weight:500;color:var(--ink)}
.why-item.active h3{color:var(--red)}
.why-item.active .why-badge{box-shadow:0 0 0 4px var(--white),0 0 0 6px var(--red)}
.why-item p{margin-top:14px;font-size:13px;line-height:19.6px;font-weight:300;color:var(--text)}

/* work */
.work{top:1361px;height:302px;background:var(--grey-bg)}
.clients{position:absolute;left:0;top:85px;width:1200px;height:64px;display:flex;background:var(--white)}
.client{flex:1;display:flex;align-items:center;justify-content:center;font-size:24px;font-weight:500;color:var(--ink)}
.gallery{position:absolute;left:0;top:150px;width:1200px;height:121px;display:flex}
.shot{position:relative;flex:1;border-right:1px solid var(--white)}
.zoom{position:absolute;right:6px;bottom:6px}

/* testimonials */
.testimonials{top:1663px;height:214px}
.quote{position:absolute;top:106px;width:420px;font-size:12.5px;line-height:19px;font-style:italic;font-weight:300;color:var(--muted)}
.quote.left{left:52px;text-align:right}
.quote.right{left:736px;text-align:left}
.who{position:absolute;top:172px;font-size:13px;font-weight:400;color:var(--ink)}
.avatar{position:absolute;top:106px;width:76px;height:76px;border-radius:50%;background:radial-gradient(circle at 50% 40%,#d8b9a3,#8c7362)}
.vline{position:absolute;left:598px;top:106px;height:82px;border-left:1.5px dashed var(--red-soft)}

/* likes */
.likes{top:1877px;height:63px;background:var(--white)}
.likes-pill{position:absolute;left:375px;top:7px;width:449px;height:45px;border:1px solid var(--line);border-radius:23px;background:var(--white);display:flex;align-items:center}
.likes-thumb{width:58px;height:100%;border-right:1px solid var(--line);display:flex;align-items:center;justify-content:center}
.likes-btn{margin-left:38px;background:#4a67ad;color:var(--white);font-size:11px;font-weight:700;border-radius:3px;padding:2px 6px}
.likes-text{margin-left:6px;font-size:11px;color:var(--ink)}

/* footer */
.site-footer{top:1940px;height:407px;background:linear-gradient(90deg,#e8363b 0%,#ee5a5d 50%,#f38484 100%);color:var(--white)}
.site-footer h4{position:absolute;top:26px;font-size:18px;font-weight:500}
.contact{position:absolute;left:52px;top:66px;width:250px;font-size:13px;line-height:19.5px;font-weight:300}
.contact p{margin-bottom:18px}
.contact b{font-weight:500}
.social{display:flex;gap:14px;margin-top:-4px}
.social span{width:14px;height:14px;border-radius:50%;background:var(--white)}
.map{position:absolute;left:333px;top:66px;width:534px;height:223px;background:linear-gradient(135deg,#e9e4d6,#cfe0ef 45%,#e6e2d4 70%,#d8d4c5)}
.map-pin{position:absolute;left:260px;top:88px}
.about{position:absolute;left:896px;top:66px;width:252px;font-size:13px;line-height:19.5px;font-weight:300}
.about p{margin-bottom:15px}
.foot-rule{position:absolute;left:52px;top:344px;width:1096px;border-top:1px solid rgba(255,255,255,.55)}
.foot-copy{position:absolute;left:52px;top:371px;font-size:12px;font-weight:500}
.foot-brand{position:absolute;left:0;width:1200px;top:360px;text-align:center;font-size:26px;font-weight:700;letter-spacing:1px}
.foot-rights{position:absolute;right:52px;top:371px;font-size:12px;font-weight:500}
</style>
</head>
<body>

<header class="hero">
  <div class="hero-photo" role="img" aria-label="City skyline behind rooftop solar panels blending into a modern lit house at dusk"></div>
  <div class="hero-ground"></div>
  <div class="hero-circle"></div>
  <div class="topbar">
    <div class="brand"><span class="brand-dot"></span>Tavo</div>
    <nav class="nav"><a>HOME</a><a>ABOUT US</a><a>SERVICES</a><a>OUR WORK</a><a>CONTACT</a></nav>
    <div class="call">Call: 13 47 29</div>
  </div>
  <h1 class="hero-title"><span>DO YOU</span><strong>NEED</strong><span>A</span><span>ELECTRICIAN</span></h1>
</header>

<section class="welcome">
  <h2 class="sec-title" style="top:16px">Welcome to <em>Tavo Electrical</em></h2>
  <div class="dots" style="top:43px"></div>
  <p>Tavo Electrical was formed to be an expert Electricity Contracting Company providing services to all Residential and Commercial Customers. With over 10 years of experience, Tavo Electrical has developed a highly-experienced team of professionals that ensure all our customer expectations are met.</p>
</section>

<section class="services">
  <h2 class="sec-title" style="top:17px">Our <em>Services</em></h2>
  <div class="dots" style="top:55px"></div>
  <div class="service" style="left:52px">
    <div class="service-photo" role="img" aria-label="Electrician testing a switchboard with a multimeter" style="background:linear-gradient(120deg,#c9c2b4,#8e8a84 50%,#3d4f8a)"></div>
    <div class="service-icon"><svg width="22" height="22" viewBox="0 0 24 24" fill="none" stroke="#fff" stroke-width="2"><path d="M5 19l4-4M14 4l-4 4 6 6 4-4zM12 6l3-3M18 12l3-3"/></svg></div>
    <div class="service-btn">Electrical</div>
  </div>
  <div class="service" style="left:426px">
    <div class="service-photo" role="img" aria-label="Warehouse ceiling fitted with bright LED high bay lights" style="background:linear-gradient(180deg,#d9dde3,#8a93a0 60%,#5b6370)"></div>
    <div class="service-icon"><svg width="22" height="22" viewBox="0 0 24 24" fill="none" stroke="#fff" stroke-width="2"><circle cx="12" cy="10" r="5"/><path d="M10 18h4M10 21h4M12 1v2M3 10H1M23 10h-2M5 3l1.5 1.5M19 3l-1.5 1.5"/></svg></div>
    <div class="service-btn">Led Lighting</div>
  </div>
  <div class="service" style="left:801px">
    <div class="service-photo" role="img" aria-label="Installers fitting solar panels on a roof" style="background:linear-gradient(150deg,#cfd8e2,#5e7490 45%,#2f4461 75%,#7f9a6e)"></div>
    <div class="service-icon"><svg width="22" height="22" viewBox="0 0 24 24" fill="none" stroke="#fff" stroke-width="2"><circle cx="12" cy="12" r="9"/><path d="M3 12h18M12 3c3 3 3 15 0 18M12 3c-3 3-3 15 0 18"/></svg></div>
    <div class="service-btn">Solar Power</div>
  </div>
</section>

<section class="why">
  <h2 class="sec-title" style="top:15px">Why <em>Choose Us</em></h2>
  <div class="dots" style="top:50px"></div>
  <div class="why-link" style="left:245px;width:146px"></div>
  <div class="why-link" style="left:525px;width:146px"></div>
  <div class="why-link" style="left:805px;width:146px"></div>
  <div class="why-item" style="left:48px">
    <div class="why-badge"><svg width="44" height="44" viewBox="0 0 24 24" fill="none" stroke="#fff" stroke-width="1.5"><circle cx="12" cy="10" r="4"/><path d="M10.5 16h3M11 19h2"/><circle cx="12" cy="11" r="8.5" stroke-dasharray="2.2 2"/></svg></div>
    <h3>Professional Service</h3>
    <p>When you hire a Tavo Electrical Electrician you will get a professional and well-presented Electrician that comes skilled and ready to do the job.</p>
  </div>
  <div class="why-item" style="left:328px">
    <div class="why-badge"><svg width="44" height="44" viewBox="0 0 24 24" fill="none" stroke="#fff" stroke-width="3" stroke-linecap="round" stroke-linejoin="round"><path d="M5 12l5 5 9-10"/></svg></div>
    <h3>5 Year Guarantee</h3>
    <p>You can buy with confidence as all of our work has a 5 year workmanship guarantee. For your peace of mind, we unconditionally back our electrical work.<br>We will come back to fix any problems at our own expense.</p>
  </div>
  <div class="why-item active" style="left:608px">
    <div class="why-badge"><svg width="44" height="44" viewBox="0 0 24 24" fill="none" stroke="#fff" stroke-width="1.6"><circle cx="12" cy="10" r="3"/><path d="M12 3v2M12 15v2M5 10h2M17 10h2M7 5l1.4 1.4M17 5l-1.4 1.4M4 17c2 3 14 3 16 0"/></svg></div>
    <h3>Environmentally friendly</h3>
    <p>We a committed to reducing carbon emissions by installing Solar Power and upgrading sites to LED Lighting. In addition to reducing the carbon emissions we recycle Fluorescent Tubes, Highbay Globes, Metal and Cardboard.</p>
  </div>
  <div class="why-item" style="left:887px">
    <div class="why-badge"><svg width="44" height="44" viewBox="0 0 24 24" fill="none" stroke="#fff" stroke-width="1.6"><rect x="3" y="6" width="18" height="13" rx="2"/><path d="M3 9l14-5 1 2M15 12h6v4h-6z"/></svg></div>
    <h3>Value for Money</h3>
    <p>We provide extremely competitive pricing, which means you get value for money on quality that is comparable to the best in the industry.</p>
  </div>
</section>

<section class="work">
  <h2 class="sec-title" style="top:16px">Our <em>Work</em></h2>
  <div class="dots" style="top:56px"></div>
  <div class="clients">
    <div class="client">Velvetine</div>
    <div class="client">Outback Supply Co</div>
    <div class="client">Plasterline</div>
    <div class="client">Marden Signs</div>
    <div class="client">Steelvane</div>
  </div>
  <div class="gallery">
    <div class="shot" role="img" aria-label="Retail store interior with new lighting" style="background:linear-gradient(180deg,#cfc8c2,#8b6f78)"><svg class="zoom" width="28" height="28" viewBox="0 0 24 24" fill="none" stroke="#fff" stroke-width="2.4"><circle cx="10" cy="10" r="6"/><path d="M14.5 14.5L20 20M10 7v6M7 10h6"/></svg></div>
    <div class="shot" role="img" aria-label="Warehouse aisles with racking under LED lights" style="background:linear-gradient(180deg,#b9b4ab,#6d655c)"><svg class="zoom" width="28" height="28" viewBox="0 0 24 24" fill="none" stroke="#fff" stroke-width="2.4"><circle cx="10" cy="10" r="6"/><path d="M14.5 14.5L20 20M10 7v6M7 10h6"/></svg></div>
    <div class="shot" role="img" aria-label="Trade supply building exterior with red front" style="background:linear-gradient(180deg,#e3c7d6 0%,#d9d3d9 35%,#c62a33 60%,#8c2025 100%)"><svg class="zoom" width="28" height="28" viewBox="0 0 24 24" fill="none" stroke="#fff" stroke-width="2.4"><circle cx="10" cy="10" r="6"/><path d="M14.5 14.5L20 20M10 7v6M7 10h6"/></svg></div>
    <div class="shot" role="img" aria-label="Sign workshop interior with high bay lighting" style="background:linear-gradient(180deg,#c8c4bd,#7a7068)"><svg class="zoom" width="28" height="28" viewBox="0 0 24 24" fill="none" stroke="#fff" stroke-width="2.4"><circle cx="10" cy="10" r="6"/><path d="M14.5 14.5L20 20M10 7v6M7 10h6"/></svg></div>
    <div class="shot" role="img" aria-label="Steel warehouse interior under industrial lights" style="background:linear-gradient(180deg,#bcc2c8,#5e646b)"><svg class="zoom" width="28" height="28" viewBox="0 0 24 24" fill="none" stroke="#fff" stroke-width="2.4"><circle cx="10" cy="10" r="6"/><path d="M14.5 14.5L20 20M10 7v6M7 10h6"/></svg></div>
  </div>
</section>

<section class="testimonials">
  <h2 class="sec-title" style="top:20px">What <em>People Say</em></h2>
  <div class="dots" style="top:58px"></div>
  <p class="quote left">Duis aute irure dolor in reprehenderit in voluptate velit esse cillum dolore eu fugiat nulla pariatur. Excepteur sint occaecat cupidatat non proident, sunt in culpa qui officia deserunt mollit.</p>
  <div class="who" style="left:263px">Mark Ellison, Operations Manager</div>
  <div class="avatar" role="img" aria-label="Portrait of Mark Ellison" style="left:488px"></div>
  <div class="vline"></div>
  <div class="avatar" role="img" aria-label="Portrait of Rosa Bennett" style="left:630px"></div>
  <p class="quote right">Provident, similique sunt in culpa qui officia deserunt mollitia animi, id est laborum et dolorum fuga. Et harum quidem rerum facilis est et expedita distinctio. Nam libero tempore, cum soluta nobis.</p>
  <div class="who" style="left:736px">Rosa Bennett, Creative Designer</div>
</section>

<section class="likes">
  <div class="likes-pill">
    <div class="likes-thumb"><svg width="20" height="20" viewBox="0 0 24 24" fill="none" stroke="#b5b5b5" stroke-width="1.6"><path d="M7 10v10H3V10zM7 10l4-7c2 0 3 1 2.5 3L13 9h6c1.5 0 2 1 2 2l-2 7c-.3 1.2-1 2-2 2H7"/></svg></div>
    <span class="likes-btn">Like</span><span class="likes-text">You and 4k others like this.</span>
  </div>
</section>

<footer class="site-footer">
  <h4 style="left:52px">Contact Us</h4>
  <div class="contact">
    <p>Please feel free to contact us for any issue. Our staff is available to you from 9AM until 5PM on weekdays.</p>
    <p><b>Phone:</b> 13 47 29</p>
    <p><b>Office:</b> 12/84 Linden Rd Glen Ashby</p>
    <p><b>Email:</b> service@tavoelectrical.com.au</p>
    <div class="social"><span></span><span></span><span></span><span></span><span></span></div>
  </div>
  <h4 style="left:333px;width:534px;text-align:center">Headquarters</h4>
  <div class="map" role="img" aria-label="Street map showing the headquarters location">
    <svg class="map-pin" width="20" height="28" viewBox="0 0 20 28"><path d="M10 0C4.5 0 0 4.5 0 10c0 7 10 18 10 18s10-11 10-18C20 4.5 15.5 0 10 0z" fill="#d9342b"/><circle cx="10" cy="10" r="3.5" fill="#8a1a15"/></svg>
  </div>
  <h4 style="left:896px">About Team</h4>
  <div class="about">
    <p>Enim congue blandit. Lorem ipsum dolor sit amet, consectetur adipiscing elit. Quisque consectetur interdum finibus. Vestibulum ante ipsum primis in faucibus orci. luctus et ultrices posuere.</p>
    <p>Cubilia cras blandit finibus ipsum, id porttitor arcu volutpat a. Integer iaculis erat nec justo malesuada faucibus vel tempus sapien. Vivamus aliquam euismod tristique.</p>
  </div>
  <div class="foot-rule"></div>
  <div class="foot-copy">Copyright © Tavo Electrical</div>
  <div class="foot-brand">Tavo</div>
  <div class="foot-rights">All rights reserved</div>
</footer>

</body>
</html>
```